Postcard Design

I am a practicing Obstetrician and Gynecologist. I am working at a clinic called Corvane Ridge Health System. I am looking for a design of a personal advertisement card that can be mailed, handed out, or sent an an electronic copy to the local newspaper to be placed as an ad. I previously worked for another clinic called TBW. They had an ad on my I liked very much, but I cannot use it. It is proprietary to them. I would like something like it. Copy attached. I want my foto and text. I have Printhollow Business Cards with Corvane Ridge and Stationary already. Access permitted. I would like to stay within that light blue - light green color scheme. I want the card to have me come across as competent and knowledgeable, but also as gentle, compassionate, benevolent, caring, knowledgeable, competent. Obviously, it has to appeal to women.

Target Market(s)

Public, patients, women

Industry/Entity Type

Electronic

Requirements
Nice to have
• A sophisticated, tasteful and inspiring maternity care image is very hard to find. I love the one on my business card. If it or something like it could be found and incorporated, that would be nice. I like a warm, soft, friendly font, Calibri light italic, Archer, Gotham. Describes nicely:Archer, the colorful slab serif. Sweet but not saccharine, earnest but not grave, Archer is designed to hit just the right notes of forthrightness, credibility, and charm.

```html
<!DOCTYPE html>
<html lang="en">
<head>
<meta charset="utf-8">
<title>Marius T. Hallworth, MD – Obstetrician &amp; Gynecologist</title>
<link rel="stylesheet" href="https://fonts.googleapis.com/css2?family=Source+Sans+3:ital,wght@0,300;0,400;0,600;1,400&display=swap">
<style>
  :root {
    --cream: #fbf5df;
    --cream-stripe: #f4f0d4;
    --photo-light: #d6dbe0;
    --photo-dark: #8a939c;
    --green: #c7df86;
    --green-soft: rgba(196, 224, 140, 0.9);
    --blue-soft: rgba(150, 211, 232, 0.8);
    --blue-pale: rgba(190, 228, 238, 0.65);
    --ink: #3b4148;
    --ink-navy: #1f3550;
    --plans-ink: #8ea3b8;
  }
  html, body {
    margin: 0;
    padding: 0;
    overflow: hidden;
    background: #ffffff;
  }
  .card {
    position: relative;
    width: 1200px;
    height: 929px;
    overflow: hidden;
    background: var(--cream);
    font-family: "Source Sans 3", "Helvetica Neue", Arial, sans-serif;
    color: var(--ink);
  }
  .card__stripe {
    position: absolute;
    left: 645px;
    top: 30px;
    width: 495px;
    height: 870px;
    background: var(--cream-stripe);
  }
  .portrait {
    position: absolute;
    left: 66px;
    top: 30px;
    width: 579px;
    height: 870px;
    background: linear-gradient(160deg, var(--photo-light) 0%, #bcc4cc 55%, var(--photo-dark) 100%);
  }
  .card__pale-band {
    position: absolute;
    left: 204px;
    top: 555px;
    width: 936px;
    height: 345px;
    background: var(--blue-pale);
  }
  .plans {
    position: absolute;
    right: 84px;
    top: 40px;
    width: 360px;
    margin: 0;
    text-align: right;
    font-size: 17px;
    line-height: 24px;
    font-weight: 300;
    color: var(--plans-ink);
  }
  .name-panel {
    position: absolute;
    left: 645px;
    top: 360px;
    width: 495px;
    height: 165px;
    background: var(--green);
    box-sizing: border-box;
    padding: 40px 0 0;
    text-align: center;
  }
  .name-panel__name {
    margin: 0;
    font-size: 48px;
    font-weight: 400;
    line-height: 1.05;
    color: var(--ink);
  }
  .name-panel__credentials {
    margin: 4px 0 0;
    font-size: 28px;
    font-weight: 400;
    color: var(--ink);
  }
  .specialty {
    position: absolute;
    left: 204px;
    top: 555px;
    width: 441px;
    height: 240px;
    background: var(--blue-soft);
    box-sizing: border-box;
    padding: 50px 0 0 36px;
    color: var(--ink-navy);
  }
  .specialty__label {
    margin: 0;
    font-size: 28px;
    font-weight: 400;
    line-height: 1.1;
  }
  .specialty__title {
    margin: 2px 0 0;
    font-size: 50px;
    font-weight: 400;
    line-height: 1.08;
  }
  .contact {
    position: absolute;
    left: 645px;
    top: 540px;
    width: 495px;
    height: 246px;
    background: var(--green-soft);
    box-sizing: border-box;
    padding: 18px 24px 0 0;
    text-align: right;
    font-size: 28px;
    line-height: 34px;
    color: var(--ink);
  }
  .contact p { margin: 0; }
  .contact__intro { font-style: italic; }
  .contact__clinic { font-weight: 600; }
</style>
</head>
<body>
  <main class="card">
    <div class="card__stripe"></div>
    <div class="portrait" role="img" aria-label="Portrait photo of the doctor smiling, wearing a white coat, against a soft grey backdrop"></div>
    <div class="card__pale-band"></div>

    <p class="plans">Credentialed Provider with<br>Alderic Global<br>Bluefern / Blueshore<br>Marlo's Choicewell<br>Statecaid, Seniorcare<br>KRP, Veltcare, Stayfair<br>Tendcare, Tridell...<br>Referral required<br>with some plans.</p>

    <section class="name-panel">
      <h1 class="name-panel__name">Marius T. Hallworth</h1>
      <p class="name-panel__credentials">MD, FACOG</p>
    </section>

    <section class="specialty">
      <p class="specialty__label">Board Certified</p>
      <h2 class="specialty__title">Obstetrician<br>&amp; Gynecologist</h2>
    </section>

    <section class="contact">
      <p class="contact__intro">Accepting New Patients at</p>
      <p class="contact__clinic">Corvane Ridge Health System</p>
      <p>214-B Calle Verano</p>
      <p>Marlow Bay, GU 96920</p>
      <p>555-014-6201</p>
      <p>Fax 555-014-0045</p>
    </section>
  </main>
</body>
</html>
```